THE PRACTICE NAME "Sunridge Care Clinic" FOR A NEW MEDICAL PRACTICE STARTUP

THIS IS A BUSINESS CARD REQUEST FOR A KIDNEY DOCTOR's(NEPHROLOGIST) PRACTICE, THIS PRACTICE WILL BE IN EL PASO,TEXAS USA.OPEN TO INNOVATIVE IDEAS!

Sunridge Care Clinic ( NAME OF PRACTICE)

VIKRANT L. MOTHRE, MD FNKF FASN ( NAME OF PHYSICIAN WITH DEGREES)
BOARD CERTIFIED INTERNAL MEDICINE
BOARD CERTIFIED NEPHROLOGY
HYPERTENSION SPECIALIST

OFFICE ADDRESS, PHONE, FAX AND EMAIL PENDING

Guarding Health. Building Futures.(MOTTO) THE LOGO SHOILD REFLECT THIS MESSAGE. WE NEED A LOGO DESIGN WITH 2 KIDNEYS OR CAN BE ONE KIDNEY ALSO.

Target Market(s)

PATIENTS WITH KIDNEY DISEASE, HYPERTENSION, ENGLISH AND SPANISH SPEAKING POPULATION AND PATIENTS ON DIALYSIS

Industry/Entity Type

Health Care

Contact Information for Business Card

HYPERTENSION SPECIALIST

WEBSITE URL PENDING

Font styles to use
Serif
Sans Serif
Script

Colors
fbed38
ffc214
fbf289
fbee3e
5c5c5c
333333
1b1b1b
757575
d3d3d3

Requirements
Must have
• A KIDNEY LOGO
• NAME OF THE PRACTICE
Nice to have
• IF THE CARD CAN BE IN THE SHAPE OF A KIDNEY

```html
<!DOCTYPE html>
<html lang="en">
<head>
<meta charset="utf-8">
<title>Sunridge Care Clinic — Business Card</title>
<link rel="stylesheet" href="https://fonts.googleapis.com/css2?family=Open+Sans:wght@400;600;700&display=swap">
<style>
  :root {
    --backdrop: #74746f;
    --card-yellow: #f2cb5a;
    --card-yellow-deep: #efc346;
    --paper: #ffffff;
    --paper-soft: #f6f6f4;
    --ink: #333333;
    --ink-soft: #5c5c5c;
    --rule: #757575;
  }
  * { box-sizing: border-box; margin: 0; padding: 0; }
  html, body {
    width: 1200px; height: 910px; overflow: hidden;
    background: var(--backdrop);
    font-family: "Open Sans", Arial, sans-serif;
  }
  .business-card {
    position: absolute; left: 100px; top: 170px;
    width: 1000px; height: 570px;
    overflow: hidden;
    box-shadow: 0 12px 30px rgba(0,0,0,0.35);
  }
  .card-background { position: absolute; inset: 0; }

  .practice-lockup {
    position: absolute; left: 45px; top: 340px;
    width: 420px;
    display: flex; flex-direction: column; align-items: center;
  }
  .practice-mark {
    display: flex; align-items: center; gap: 14px;
  }
  .mark-dot {
    width: 40px; height: 40px; border-radius: 50%;
    background: var(--card-yellow-deep);
    flex: none;
  }
  .practice-name {
    color: var(--ink-soft);
    font-weight: 600; font-size: 28px; line-height: 1.1;
    white-space: nowrap;
  }
  .practice-rule {
    width: 300px; height: 1px; background: var(--rule);
    margin-top: 14px;
  }
  .practice-motto {
    margin-top: 5px;
    font-size: 12px; color: var(--ink-soft); letter-spacing: 0.3px;
  }

  .physician-block { position: absolute; left: 440px; top: 110px; }
  .physician-name {
    display: inline-block;
    background: var(--paper);
    border-radius: 30px;
    padding: 8px 26px 8px 22px;
    color: var(--ink);
    font-size: 33px; font-weight: 400; letter-spacing: 0.5px;
    white-space: nowrap;
  }
  .physician-credentials { font-size: 16px; margin-left: 4px; }
  .physician-titles {
    list-style: none;
    margin: 8px 0 0 26px;
    color: var(--paper);
    font-size: 15px; line-height: 1.25; letter-spacing: 0.6px;
    text-transform: uppercase;
  }

  .contact-list {
    position: absolute; left: 610px; top: 265px;
    list-style: none;
  }
  .contact-item {
    display: flex; align-items: center; gap: 16px;
    height: 46px;
    color: var(--ink); font-size: 20px;
  }
  .contact-icon {
    width: 30px; height: 30px; border-radius: 50%;
    background: var(--ink);
    display: flex; align-items: center; justify-content: center;
    flex: none;
  }
  .contact-icon svg { width: 17px; height: 17px; }
</style>
</head>
<body>
  <article class="business-card">
    <svg class="card-background" viewBox="0 0 1000 570" width="1000" height="570" aria-hidden="true">
      <defs>
        <linearGradient id="cardYellow" x1="0" y1="0" x2="1" y2="1">
          <stop offset="0" stop-color="#f4d064"/>
          <stop offset="1" stop-color="#efc346"/>
        </linearGradient>
      </defs>
      <rect width="1000" height="570" fill="url(#cardYellow)"/>
      <path d="M1000 230 Q 930 500 560 570 L 1000 570 Z" fill="#f6f6f4"/>
      <rect x="982" y="0" width="18" height="570" fill="#f6f6f4"/>
      <circle cx="255" cy="420" r="255" fill="#ffffff"/>
    </svg>

    <div class="practice-lockup">
      <div class="practice-mark">
        <span class="mark-dot"></span>
        <div class="practice-name">Sunridge Care Clinic</div>
      </div>
      <div class="practice-rule"></div>
      <p class="practice-motto">Guarding Health. Building Futures.</p>
    </div>

    <section class="physician-block">
      <h1 class="physician-name">VIKRANT L. MOTHRE,<span class="physician-credentials">MD FNKF FASN</span></h1>
      <ul class="physician-titles">
        <li>Board Certified Internal Medicine</li>
        <li>Board Certified Nephrology</li>
        <li>Hypertension Specialist</li>
      </ul>
    </section>

    <ul class="contact-list">
      <li class="contact-item">
        <span class="contact-icon"><svg viewBox="0 0 24 24"><rect x="3" y="6" width="18" height="12" rx="1" fill="none" stroke="#fff" stroke-width="2"/><path d="M3 7 L12 13 L21 7" fill="none" stroke="#fff" stroke-width="2"/></svg></span>
        email@email.com
      </li>
      <li class="contact-item">
        <span class="contact-icon"><svg viewBox="0 0 24 24"><path d="M6.6 10.8a15 15 0 0 0 6.6 6.6l2.2-2.2c.3-.3.7-.4 1-.2 1.1.4 2.3.6 3.6.6.6 0 1 .4 1 1V20c0 .6-.4 1-1 1A17 17 0 0 1 3 4c0-.6.4-1 1-1h3.5c.6 0 1 .4 1 1 0 1.3.2 2.5.6 3.6.1.3 0 .7-.2 1z" fill="#fff"/></svg></span>
        Phone Number
      </li>
      <li class="contact-item">
        <span class="contact-icon"><svg viewBox="0 0 24 24"><path d="M12 2a7 7 0 0 0-7 7c0 5 7 13 7 13s7-8 7-13a7 7 0 0 0-7-7zm0 9.5A2.5 2.5 0 1 1 12 6.5a2.5 2.5 0 0 1 0 5z" fill="#fff"/></svg></span>
        Office Address
      </li>
      <li class="contact-item">
        <span class="contact-icon"><svg viewBox="0 0 24 24"><circle cx="12" cy="12" r="9" fill="none" stroke="#fff" stroke-width="2"/><ellipse cx="12" cy="12" rx="4" ry="9" fill="none" stroke="#fff" stroke-width="2"/><path d="M3 12h18" stroke="#fff" stroke-width="2"/></svg></span>
        www.pendingurl.com
      </li>
    </ul>
  </article>
</body>
</html>
```